Company notecard redesign

We'd like a redesign done of our company notecards. We use these cards to hand-write messages to clients/potential clients. This could be thank-you cards, congratulations cards, check-in cards, etc. Current cards are 5.5" x 8.5" and fold in half (you'll see the fold mark on the scanned image). We would like the new cards to not fold, and just be 5.5" x 4.25". We do like the little dog head you'll see on the inside notecard scan as the dog is our logo. I've also attached our "professional" logo with our new tagline. Address info you see on the outside notecard scan is correct.

Target Market(s)

Salesforce and CRM clients

Industry/Entity Type

It Company

Colors
3377b5
ffffff
fff8ef

Requirements
Must have
• Our logo, some contact info
Nice to have
• Dog head from our current notecard scan

```html
<!DOCTYPE html>
<html lang="en">
<head>
<meta charset="utf-8">
<title>Harlow Notecard</title>
<link rel="stylesheet" href="https://fonts.googleapis.com/css2?family=PT+Sans+Narrow:wght@400;700&family=Questrial&display=swap">
<style>
  :root {
    --navy: #0c3049;
    --sky: #7aaecd;
    --grey: #9a9a9a;
    --paper: #ffffff;
  }
  * { margin: 0; padding: 0; box-sizing: border-box; }
  html, body { width: 1200px; height: 927px; overflow: hidden; background: var(--paper); }
  .card { position: relative; width: 1200px; height: 927px; background: var(--paper); }
  .edge-bar {
    position: absolute; left: 754px; width: 119px; height: 24px; background: var(--navy);
  }
  .edge-bar--top { top: 0; }
  .edge-bar--bottom { top: 903px; }
  .greeting {
    position: absolute; left: 751px; top: 42px;
    font-family: "PT Sans Narrow", sans-serif; font-weight: 400;
    font-size: 58px; line-height: 1; color: var(--sky); letter-spacing: 1px;
  }
  .brand {
    position: absolute; left: 328px; top: 383px; width: 545px; height: 165px;
  }
  .brand__name {
    position: absolute; left: 0; top: 0;
  }
  .brand__mark {
    position: absolute; left: 757px; top: 386px; width: 114px; height: 114px;
    border-radius: 50%; background: var(--sky);
  }
  .brand__tagline {
    position: absolute; left: 330px; top: 519px;
    font-family: "Questrial", sans-serif; font-size: 27px; line-height: 1;
    letter-spacing: 4.3px; color: var(--grey); white-space: nowrap;
  }
  .address {
    position: absolute; left: 754px; top: 784px;
    font-family: "PT Sans Narrow", sans-serif; font-size: 20.5px;
    line-height: 25.7px; color: var(--sky); font-style: normal;
  }
</style>
</head>
<body>
  <main class="card">
    <div class="edge-bar edge-bar--top"></div>
    <p class="greeting">HELLO</p>

    <svg class="brand__name" style="position:absolute;left:328px;top:383px" width="412" height="122" viewBox="0 0 412 122" aria-label="Harlow">
      <text x="0" y="120" textLength="410" lengthAdjust="spacingAndGlyphs"
            font-family="PT Sans Narrow, sans-serif" font-weight="700" font-size="168"
            fill="#0c3049">HARLOW</text>
    </svg>
    <div class="brand__mark" aria-hidden="true"></div>
    <p class="brand__tagline">A CLOUD CONSULTING COMPANY</p>

    <address class="address">
      3180 E 54th St.<br>
      Suite 7<br>
      Lakeview, IN<br>
      46290, USA
    </address>
    <div class="edge-bar edge-bar--bottom"></div>
  </main>
</body>
</html>
```